Brava Stone Oven Kitchen (restaurant)

Restaurant with a cool vibe.
We need a refresh of existing site. Appealing to a hip crowd of 25 or older age bracket (mid price to high small town). Constant changes food and cocktail menu. A vibing atmosphere with jazz funk hip music.
Must be able to scale for any device… phone/mobile device super important.
Instagram: @Brava.Linwell
Website: bravalinwell.example

Target Market(s)

25-55 age group

Number of Pages Required

1 page

Font styles to use
Sans Serif

Requirements
Must have
• Simple to navigate. Simplicity is the key to all sophistication.

Links/Buttons
Menu
Gift Cards
Reservations
Take Out
Contact Us
Should not have
• Please, nothing generic looking… no cookie cutter look. Originality

```html
<!DOCTYPE html>
<html lang="en">
<head>
<meta charset="utf-8">
<title>Brava Stone Oven Kitchen</title>
<link href="https://fonts.googleapis.com/css2?family=Montserrat:wght@600;700&family=Roboto:wght@400;500;700&display=swap" rel="stylesheet">
<style>
:root{
  --red:#ff0000;
  --black:#0d0d0d;
  --dark:#161616;
  --panel:#0f0f0f;
  --white:#ffffff;
  --muted:#d8d8d8;
}
*{margin:0;padding:0;box-sizing:border-box}
html,body{width:1200px;height:2877px;overflow:hidden;background:var(--dark)}
body{position:relative;font-family:'Roboto',sans-serif;color:var(--white)}
.abs{position:absolute}
.btn{position:absolute;display:flex;align-items:center;justify-content:center;font-family:'Roboto',sans-serif;font-weight:700;font-size:15px;text-transform:uppercase;text-decoration:none}
.btn-red{background:var(--red);color:var(--white)}
.btn-white{background:var(--white);color:#111}
.heading{font-family:'Montserrat',sans-serif;font-weight:700;text-transform:uppercase}

/* header */
.site-header{left:0;top:0;width:1200px;height:86px;background:#1c1c1c}
.brand{position:absolute;text-align:center;font-family:'Montserrat',sans-serif;color:var(--white)}
.brand-name{display:block;font-weight:700;font-size:42px;letter-spacing:3px;line-height:42px}
.brand-sub{display:block;font-family:'Roboto',sans-serif;font-size:16px;letter-spacing:.5px;line-height:18px}
.main-nav{left:425px;top:34px;display:flex;gap:23px;font-weight:500;font-size:15.5px}
.main-nav a{color:var(--white);text-decoration:none}

/* hero */
.hero{left:0;top:86px;width:1200px;height:599px;background:radial-gradient(ellipse at 25% 30%,#9c8a74 0%,#5a4a3a 35%,#2b2a22 65%,#1c2416 100%)}
.hero-shade{left:0;top:86px;width:1200px;height:599px;background:rgba(0,0,0,.25)}
.hero-kicker{left:0;top:298px;width:1200px;text-align:center;font-size:31px}
.hero-title{left:0;top:340px;width:1200px;text-align:center;font-size:40px}

/* story */
.story-photo{left:112px;top:781px;width:488px;height:386px;background:linear-gradient(180deg,#b8c2cc 0%,#9a6a52 35%,#7a4a36 70%,#4b5560 100%)}
.story-card{left:573px;top:805px;width:515px;height:338px;background:var(--panel)}
.story-title{left:613px;top:826px;font-size:35px}
.story-text{left:613px;top:887px;width:434px;font-size:15px;line-height:24px;text-align:justify;color:var(--white)}

/* menus */
.menus{left:0;top:1263px;width:1200px;height:571px;background:radial-gradient(ellipse at 50% 50%,#1e2a3a 0%,#141b26 60%,#0b0f15 100%)}
.menus-title{left:0;top:1316px;width:1200px;text-align:center;font-size:33px}
.menu-card{position:absolute;top:1403px;width:230px;height:268px;background:var(--white)}
.menu-photo{width:230px;height:215px}
.menu-label{height:53px;display:flex;align-items:center;justify-content:center;color:#111;font-weight:500;font-size:19.5px;text-transform:uppercase}

/* gift */
.gift-red{left:112px;top:1929px;width:481px;height:300px;background:var(--red)}
.gift-photo{left:593px;top:1929px;width:496px;height:300px;background:radial-gradient(ellipse at 45% 55%,#c9a36a 0%,#8a9a4a 40%,#6b4a2a 75%,#3a3a3a 100%)}
.gift-title{left:112px;top:1990px;width:481px;text-align:center;font-size:36px}
.gift-sub{left:112px;top:2048px;width:481px;text-align:center;font-size:29px;font-weight:500}

/* mailing */
.mailing{left:0;top:2327px;width:1200px;height:238px;background:radial-gradient(ellipse at 50% 50%,#3a2a34 0%,#24202a 55%,#141414 100%)}
.mailing-title{left:0;top:2376px;width:1200px;text-align:center;font-family:'Montserrat',sans-serif;font-weight:700;font-size:25px}
.mailing-rule{left:490px;top:2418px;width:220px;height:2px;background:var(--white)}
.email-field{left:257px;top:2461px;width:686px;height:50px;background:var(--white);color:#666;font-size:15px;padding:15px 16px}

/* footer */
.site-footer{left:0;top:2565px;width:1200px;height:312px;background:var(--black)}
.foot-head{font-weight:500;font-size:17.5px}
.foot-line{font-size:15.5px;line-height:25px;color:var(--white);white-space:nowrap}
.foot-icon{position:absolute;width:14px;height:14px}
.foot-rule{left:111px;width:978px;height:1px;background:#9a9a9a}
.foot-nav{left:111px;top:2771px;display:flex;gap:23px;font-weight:700;font-size:15.5px;text-transform:uppercase}
.social{position:absolute;top:2763px;width:36px;height:36px;border-radius:50%;background:var(--white)}
.legal{font-size:12.5px}
</style>
</head>
<body>

<header class="abs site-header">
  <div class="brand" style="left:112px;top:12px;width:200px">
    <span class="brand-name">BRAVA</span>
    <span class="brand-sub">Stone Oven Kitchen</span>
  </div>
  <nav class="abs main-nav">
    <a href="#">Home</a><a href="#">About Us</a><a href="#">Menus</a><a href="#">Order Online</a><a href="#">Reservations</a>
  </nav>
  <a class="btn btn-red" href="#" style="left:943px;top:18px;width:143px;height:49px">Contact Us</a>
</header>

<section>
  <div class="abs hero" role="img" aria-label="Close-up photo of grilled chicken with salad greens"></div>
  <div class="abs hero-shade"></div>
  <h2 class="abs heading hero-kicker">Welcome to</h2>
  <h1 class="abs heading hero-title">Brava Stone Oven Kitchen</h1>
  <a class="btn btn-red" href="#" style="left:448px;top:415px;width:142px;height:49px">Reservations</a>
  <a class="btn btn-white" href="#" style="left:609px;top:415px;width:144px;height:49px">Take Out</a>
</section>

<section>
  <div class="abs story-photo" role="img" aria-label="Photo of the restaurant's brick building on a street corner"></div>
  <div class="abs story-card"></div>
  <h2 class="abs heading story-title">Our Story</h2>
  <p class="abs story-text">Lorem ipsum dolor sit amet, consectetur adipiscing elit, sed do eiusmod tempor incididunt ut labore et dolore magna aliqua. Ut enim ad minim veniam, quis nostrud exercitation ullamco laboris nisi ut aliquip ex ea commodo consequat. Duis aute irure dolor in reprehenderit in voluptate velit esse. Nostrud exercitation ullamco laboris nisi ut aliquip ex ea commodoa.</p>
  <a class="btn btn-red" href="#" style="left:613px;top:1063px;width:144px;height:50px">Learn More</a>
</section>

<section>
  <div class="abs menus" role="img" aria-label="Dark table top with cookies, tea and spices"></div>
  <h2 class="abs heading menus-title">Check Out Our Menus</h2>
  <div class="menu-card" style="left:112px"><div class="menu-photo" role="img" aria-label="Photo of tacos with cabbage" style="background:linear-gradient(160deg,#6a4a6a,#8a5a2a 60%,#e8e0d0)"></div><div class="menu-label">Shareables</div></div>
  <div class="menu-card" style="left:360px"><div class="menu-photo" role="img" aria-label="Photo of stone oven pizzas" style="background:linear-gradient(160deg,#d8c8a8,#b07a48 55%,#8a3a2a)"></div><div class="menu-label">Wood Fired Pizza</div></div>
  <div class="menu-card" style="left:610px"><div class="menu-photo" role="img" aria-label="Photo of bowls of dips" style="background:linear-gradient(160deg,#9a9a88,#6a7a3a 45%,#c07a3a)"></div><div class="menu-label">Salads</div></div>
  <div class="menu-card" style="left:858px"><div class="menu-photo" role="img" aria-label="Photo of a toasted sandwich" style="background:linear-gradient(160deg,#b0a888,#e0c078 50%,#c89a8a)"></div><div class="menu-label">Sandwiches</div></div>
  <svg class="abs" style="left:40px;top:1527px" width="24" height="22" viewBox="0 0 24 22" aria-label="Previous"><path d="M11 2 2 11l9 9M2 11h20" fill="none" stroke="#999" stroke-width="4"/></svg>
  <svg class="abs" style="left:1134px;top:1527px" width="24" height="22" viewBox="0 0 24 22" aria-label="Next"><path d="M13 2l9 9-9 9M22 11H2" fill="none" stroke="#ff0000" stroke-width="4"/></svg>
  <a class="btn btn-red" href="#" style="left:518px;top:1722px;width:163px;height:49px">View All Menu</a>
</section>

<section>
  <div class="abs gift-red"></div>
  <div class="abs gift-photo" role="img" aria-label="Photo of a burger with guacamole and tomato"></div>
  <h2 class="abs heading gift-title">Gift Card</h2>
  <p class="abs gift-sub">Get Voucher 20% OFF</p>
  <a class="btn btn-white" href="#" style="left:280px;top:2110px;width:144px;height:49px;color:var(--red)">Get Free</a>
</section>

<section>
  <div class="abs mailing" role="img" aria-label="Dark blurred photo of fresh salad"></div>
  <h2 class="abs mailing-title">Join Our Mailing For Discounts</h2>
  <div class="abs mailing-rule"></div>
  <div class="abs email-field">Email Address</div>
  <a class="btn btn-red" href="#" style="left:794px;top:2465px;width:145px;height:42px">Subscribe</a>
</section>

<footer class="abs site-footer"></footer>
<div class="brand" style="left:112px;top:2628px;width:200px">
  <span class="brand-name">BRAVA</span>
  <span class="brand-sub">Stone Oven Kitchen</span>
</div>

<div class="abs foot-head" style="left:377px;top:2621px">Our Location</div>
<svg class="foot-icon" style="left:376px;top:2663px" viewBox="0 0 14 14"><path d="M7 1a4 4 0 0 0-4 4c0 3 4 8 4 8s4-5 4-8a4 4 0 0 0-4-4z" fill="#ff0000"/><circle cx="7" cy="5" r="1.5" fill="#0d0d0d"/></svg>
<div class="abs foot-line" style="left:410px;top:2657px">48 Harrow Lane<br>Linwell, ON</div>

<div class="abs foot-head" style="left:608px;top:2623px">Opening Hours</div>
<svg class="foot-icon" style="left:609px;top:2664px" viewBox="0 0 14 14"><circle cx="7" cy="7" r="5.5" fill="none" stroke="#ff0000" stroke-width="1.6"/><path d="M7 4v3.5h2.5" fill="none" stroke="#ff0000" stroke-width="1.6"/></svg>
<div class="abs foot-line" style="left:643px;top:2657px">Thursday to Sunday<br>12:00pm – 9:00pm</div>

<div class="abs foot-head" style="left:870px;top:2621px">Contact Us</div>
<svg class="foot-icon" style="left:870px;top:2660px" viewBox="0 0 14 14"><path d="M3 1l2.5 3-1.5 1.5c1 2 2.5 3.5 4.5 4.5L10 8.5l3 2.5-1.5 2C6 13 1 8 1 2.5z" fill="#ff0000"/></svg>
<div class="abs foot-line" style="left:904px;top:2654px">555-014-2298</div>
<svg class="foot-icon" style="left:870px;top:2690px" viewBox="0 0 14 14"><rect x="1" y="2.5" width="12" height="9" fill="none" stroke="#ff0000" stroke-width="1.4"/><path d="M1 3l6 5 6-5" fill="none" stroke="#ff0000" stroke-width="1.4"/></svg>
<div class="abs foot-line" style="left:904px;top:2684px;font-size:14.5px">hello@bravalinwell.example</div>

<div class="abs foot-rule" style="top:2755px"></div>
<nav class="abs foot-nav"><span>Home</span><span>About Us</span><span>Menus</span><span>Order Online</span><span>Reservations</span></nav>
<a class="social" href="#" aria-label="Social link 1" style="left:966px"></a>
<a class="social" href="#" aria-label="Social link 2" style="left:1009px"></a>
<a class="social" href="#" aria-label="Follow @Brava.Linwell" style="left:1052px"></a>
<div class="abs foot-rule" style="top:2809px"></div>
<div class="abs legal" style="left:111px;top:2824px">Copyrights 2021 Company Name. All Rights Reserved</div>
<div class="abs legal" style="left:863px;top:2824px">Privacy Policy &nbsp;&nbsp;&nbsp;| &nbsp;&nbsp;&nbsp;Terms &amp; Conditions</div>

</body>
</html>
```